Business Card and Letterhead Design for Public Accounting Firm

Business card and letterhead design for a CPA Firm located in Orange County, CA. We're looking for a modern and professional design utilizing our existing logo. We'd like a clean "less is more" look, but also something that catches the eye. We provide a high level of service to our clients. Open to single or double sided business cards.

Additional info: color numbers on logo
Blue :
R 0
G 83
B 125

#00537D

Silver :

R 154
G 154
B 154

#9A9A9A

Target Market(s)

Businesses and individuals

Industry/Entity Type

Accounting

Contact Information for Business Card

Moss Whitfield & Danby LLP - 4827 Larkspur Vale Road, Irvine, CA 92614 - (949)731-2864 - mwdaccts.example

Font styles to use
Serif
Sans Serif
Other font styles liked:
• See font file uploaded

Colors
0054AA
0677BA
7BADD7
CADEEF
E8F1F8

Requirements
Nice to have
• Possibly use the font file provided which matches our logo, but adjust to be not in all caps

```html
<!DOCTYPE html>
<html lang="en">
<head>
<meta charset="utf-8">
<title>Moss Whitfield &amp; Danby LLP — Business Card</title>
<link rel="stylesheet" href="https://fonts.googleapis.com/css2?family=Cinzel:wght@500&family=Crimson+Text:wght@400&display=swap">
<style>
  :root {
    --backdrop: #e9ebee;
    --card-back: #7d7e82;
    --card-front: #ffffff;
    --brand-blue: #00537d;
    --brand-silver: #9a9a9a;
    --ink: #55575b;
    --rule: #8a8c90;
    --on-dark: #ffffff;
  }
  * { box-sizing: border-box; margin: 0; padding: 0; }
  html, body {
    width: 1200px; height: 874px; overflow: hidden;
    background: var(--backdrop);
  }
  .canvas {
    position: relative; width: 1200px; height: 874px;
  }
  .card {
    position: absolute; left: 280px; width: 640px; height: 366px;
    border-radius: 22px;
    box-shadow: 0 6px 18px rgba(0,0,0,0.18);
  }
  .card--back { top: 46px; background: var(--card-back); }
  .card--front { top: 462px; background: var(--card-front); }

  .wordmark {
    position: absolute;
    font-family: "Cinzel", serif; font-weight: 500;
    letter-spacing: 2px; line-height: 1.1;
  }
  .card--back .wordmark {
    left: 0; right: 0; top: 150px; text-align: center;
    font-size: 30px; color: var(--on-dark);
  }
  .card--front .wordmark {
    right: 48px; top: 50px; text-align: right;
    font-size: 21px; color: var(--brand-blue);
  }

  .person { position: absolute; left: 48px; top: 126px; width: 250px; }
  .person__name {
    font-family: "Cinzel", serif; font-weight: 500;
    font-size: 22px; line-height: 28px; color: var(--brand-blue); letter-spacing: 1px;
  }
  .person__title {
    font-family: "Crimson Text", serif; font-size: 15px; line-height: 20px; color: var(--ink);
    padding-bottom: 6px; border-bottom: 1px solid var(--rule);
  }
  .contact { list-style: none; margin-top: 8px; }
  .contact li {
    display: flex; align-items: center; gap: 9px;
    font-family: "Crimson Text", serif; font-size: 15px; color: var(--ink);
    line-height: 21px;
  }
  .contact svg { width: 11px; height: 11px; flex: none; fill: var(--brand-blue); }

  .divider {
    position: absolute; left: 48px; right: 48px; top: 268px;
    border-top: 1px solid var(--rule);
  }
  .address {
    position: absolute; right: 48px; top: 278px; text-align: right;
    font-family: "Crimson Text", serif; font-style: normal;
    font-size: 15px; color: var(--ink); line-height: 19px;
  }
  .address__firm {
    padding-bottom: 3px; margin-bottom: 3px;
    border-bottom: 1px solid var(--rule);
  }
</style>
</head>
<body>
<main class="canvas">
  <section class="card card--back">
    <p class="wordmark">Moss Whitfield<br>&amp; Danby LLP</p>
  </section>

  <section class="card card--front">
    <p class="wordmark">Moss Whitfield<br>&amp; Danby LLP</p>

    <div class="person">
      <h1 class="person__name">Daniel Harper</h1>
      <p class="person__title">Managing Director</p>
      <ul class="contact">
        <li>
          <svg viewBox="0 0 12 12" aria-hidden="true"><path d="M2.5 0.5 L4.5 0.5 L5.5 3.5 L4 4.5 Q5 7 7.5 8 L8.5 6.5 L11.5 7.5 L11.5 9.5 Q11 11.5 9 11.5 Q1 11 0.5 3 Q0.5 1 2.5 0.5 Z"/></svg>
          (949)731-2864
        </li>
        <li>
          <svg viewBox="0 0 12 12" aria-hidden="true"><path d="M0 2 H12 V10 H0 Z"/><path d="M0.8 2.6 L6 6.6 L11.2 2.6" fill="none" stroke="#fff" stroke-width="1"/></svg>
          info@mwdaccts.example
        </li>
        <li>
          <svg viewBox="0 0 12 12" aria-hidden="true"><circle cx="6" cy="6" r="5.5"/></svg>
          www.mwdaccts.example
        </li>
      </ul>
    </div>

    <div class="divider"></div>

    <address class="address">
      <div class="address__firm">Moss Whitfield &amp; Danby LLP</div>
      4827 Larkspur Vale Road<br>
      Irvine, CA 92614
    </address>
  </section>
</main>
</body>
</html>
```